Letterhead and Business Card for Wealth Management Company
Harborline Wealth Management
Letterhead and Business Card for Wealth Management Company - Financial Services
Creative Brief
Use same font as used in my logo
Can use the same font or add additional font
Professional
R. Dwight Voss, CRPC®
Wealth Advisor
2450 Fernbrook Avenue Suite 310 Berwyn, PA 19312
dvoss@harborline-wealth.com
www.harborline-wealth.com
I work with affluent people so I want a sophisticated and classic looking business card and stationary. Our tagline is Dream. Plan. Live. with Live in italics. You can see it on our website at www.harborline-wealth.com. If appropriate, please include the tagline on the business card, letterhead and envelope. Please note the tagline on the website is a gradient color. It looks better printed in solid color.
Be creative.
dvoss dvoss
Thanks for all the great designs! I have a busy schedule today, but I will go through them and give star ratings later today or tonight. Thanks again!
Qwirk Qwirk

```html
<!DOCTYPE html>
<html lang="en">
<head>
<meta charset="utf-8">
<title>Harborline Wealth Management – Business Card</title>
<link href="https://fonts.googleapis.com/css2?family=Cinzel:wght@600&family=Montserrat:wght@400;500;600&display=swap" rel="stylesheet">
<style>
  :root {
    --navy: #14295c;
    --gold: #c89a4a;
    --gold-light: #d9b06a;
    --paper: #ffffff;
    --backdrop: #e4e5e7;
    --ink: #3a3f4a;
  }
  * { margin: 0; padding: 0; box-sizing: border-box; }
  html, body { width: 1200px; height: 895px; overflow: hidden; }
  body {
    background: var(--backdrop);
    font-family: "Montserrat", Arial, sans-serif;
    position: relative;
  }
  .card {
    position: absolute;
    left: 250px;
    width: 700px;
    height: 400px;
    background: var(--paper);
    box-shadow: 0 6px 18px rgba(0,0,0,0.12);
    overflow: hidden;
  }
  .card--front { top: 30px; }
  .card--back { top: 465px; }

  .brand {
    position: absolute;
    display: flex;
    align-items: center;
    gap: 18px;
  }
  .brand__mark {
    width: 46px; height: 46px;
    background: var(--gold);
    flex: none;
  }
  .brand__name {
    font-family: "Cinzel", Georgia, serif;
    font-weight: 600;
    color: var(--navy);
    line-height: 1.05;
  }
  .card--front .brand { left: 130px; top: 150px; }
  .card--front .brand__name { font-size: 40px; }
  .card--front .brand__mark { width: 70px; height: 70px; }

  .card--back .brand { left: 70px; top: 40px; }
  .card--back .brand__name { font-size: 26px; }

  .gold-band {
    position: absolute;
    left: 0; top: 132px;
    width: 230px; height: 56px;
    background: linear-gradient(90deg, var(--gold), var(--gold-light));
  }
  .navy-band {
    position: absolute;
    left: 240px; top: 200px;
    right: 0; height: 52px;
    background: var(--navy);
    display: flex; align-items: center;
    padding-left: 26px;
    color: #fff;
    font-size: 15px;
    letter-spacing: 0.5px;
  }
  .person {
    position: absolute;
    left: 480px; top: 128px;
  }
  .person__name {
    color: var(--gold);
    font-size: 22px;
    font-weight: 500;
    letter-spacing: 1px;
  }
  .person__role {
    color: var(--navy);
    font-size: 15px;
    font-weight: 500;
    letter-spacing: 1px;
    margin-top: 2px;
  }
  .contact-list, .web-list {
    position: absolute;
    list-style: none;
    font-size: 12px;
    color: var(--ink);
  }
  .contact-list { left: 26px; top: 204px; }
  .web-list { left: 420px; top: 290px; }
  .contact-list li, .web-list li {
    display: flex; align-items: center; gap: 10px;
    height: 26px;
  }
  .icon {
    width: 16px; height: 16px;
    background: var(--navy);
    display: flex; align-items: center; justify-content: center;
    flex: none;
  }
  .icon--round { border-radius: 50%; }
</style>
</head>
<body>
  <section class="card card--front" aria-label="Business card front">
    <div class="brand">
      <span class="brand__mark"></span>
      <span class="brand__name">Harborline<br>Wealth Management</span>
    </div>
  </section>

  <section class="card card--back" aria-label="Business card back">
    <div class="gold-band"></div>
    <div class="brand">
      <span class="brand__mark"></span>
      <span class="brand__name">Harborline<br>Wealth Management</span>
    </div>
    <div class="person">
      <p class="person__name">DANA REYES</p>
      <p class="person__role">MANAGER</p>
    </div>
    <ul class="contact-list">
      <li><span class="icon"><svg width="10" height="10" viewBox="0 0 10 10"><path d="M5 0.5a3 3 0 0 1 3 3c0 2.3-3 6-3 6s-3-3.7-3-6a3 3 0 0 1 3-3z" fill="#fff"/></svg></span>Street country 123</li>
      <li><span class="icon"><svg width="10" height="10" viewBox="0 0 10 10"><path d="M2 1l2 2-1 1.2c.6 1.3 1.5 2.2 2.8 2.8L7 6l2 2-1.4 1.5C4.3 9 1 5.7.5 2.4z" fill="#fff"/></svg></span>012 345 6789</li>
      <li><span class="icon"><svg width="10" height="8" viewBox="0 0 10 8"><rect x="0.5" y="0.5" width="9" height="7" fill="none" stroke="#fff"/><path d="M0.5 0.5l4.5 4 4.5-4" fill="none" stroke="#fff"/></svg></span>urmail@email.com</li>
    </ul>
    <div class="navy-band">www.urwebsitename.com/123</div>
    <ul class="web-list">
      <li><span class="icon icon--round"></span>www.urwebsitename.com</li>
      <li><span class="icon icon--round"></span>www.chirpline.com</li>
      <li><span class="icon icon--round"></span>www.friendpage.com</li>
    </ul>
  </section>
</body>
</html>
```